New design for a hotel booking website

I am looking to re-design my hotel booking website pinecrestlodgings.net. Please find the specs attached. Delivery in PSD format. Two pages total: (i) homepage and (ii) inner page.
I want the design to be very simple to navigate and have a feel that is related to Banff, Canada. You can keep a similar layout as the current website.
Requirements
1) Homepage
- Booking form above the fold containing the check in & check out dates, # of rooms and the Search button
- Quality image relating to the city of Banff to make it clear what city this is (no slider - I don't want any animation)
- A section for featured hotels (3-5 items)
- A section for links to other sections on the website (currently under "Explore Banff")
- A section for articles and local guides
- A weather widget (either in the header or somewhere else, similar to this one http://clipvuebox.com/t/QX7RKLd4P2)
2) Hotel listings page - http://www.pinecrestlodgings.net/hotels
- Left or right sidebar – must contain the booking form with the same fields as on the homepage
- A section of why to book hotels with us under the booking form
- Each hotel listing should contain the following
Hotel name
Star rating
Short description (same as currently on the website)
Thumbnail
Address
A button to Check Rates
Notes
- I want the design to be user friendly, simple and easy to use
- I want it to be related to Banff. Banff is a resort town in Alberta, Canada with mountains for skiing in the winter and parks and wildlife nature in the summer.
- Delivery format: PSD
- I want the layout to be easily convertible into a responsive design
- Small social media icon to the Chatterly page (with the option to add Vidloom and Quibbit in the future)
Some competing website examples:
1) ridgemoorvale.com/Places-to-Stay/Hotels-Inns
2) torvikinns.org
Some examples of websites I liked:
1) http://www.glendrova.com/accommodation/hotels/
2) http://www.lodgetrailmarvenby.com/
Anyone looking to book their stay in Banff, AB, Canada.
Travel
2 page

```html
<!DOCTYPE html>
<html lang="en">
<head>
<meta charset="utf-8">
<title>PinecrestLodgings – Compare prices on accommodations in Banff</title>
<link rel="stylesheet" href="https://fonts.googleapis.com/css2?family=Roboto:wght@300;400;500&family=Roboto+Condensed:wght@400;700&display=swap">
<style>
:root{
  --sky-top:#b7def3;
  --sky-bottom:#f4f9fd;
  --blue:#2a9be0;
  --blue-dark:#1f7fc0;
  --ink:#2b2b2b;
  --ink-soft:#444;
  --grey:#888;
  --line:#dcdcdc;
  --panel:#ffffff;
  --dark:#3a3a3c;
  --search-bg:rgba(40,40,42,.92);
  --orange:#f7931e;
}
*{box-sizing:border-box;margin:0;padding:0}
html,body{width:993px;height:1200px;overflow:hidden}
body{position:relative;font-family:"Roboto",sans-serif;color:var(--ink);
  background:linear-gradient(180deg,var(--sky-top) 0,#d6ecf8 500px,var(--sky-bottom) 950px,#ffffff 1200px)}
a{text-decoration:none;color:inherit}
.abs{position:absolute}

/* header */
.brand{left:91px;top:14px}
.brand-name{font:500 25px/1 "Roboto",sans-serif;color:var(--blue);letter-spacing:-.3px}
.brand-tag{font:400 7.5px/1 "Roboto",sans-serif;color:var(--grey);margin-top:4px;letter-spacing:.2px}
.promo{left:390px;top:27px;font-size:10.5px;color:var(--blue)}
.promo span{color:#5aa7d8}
.round-icon{width:30px;height:30px;border-radius:50%;background:var(--blue)}
.promo-icon{left:723px;top:18px}
.weather{left:769px;top:26px;font-size:10px;color:var(--ink-soft)}
.weather-icon{left:841px;top:17px;width:31px;height:31px;border:2px solid var(--blue);border-radius:50%;background:#fff}
.temp{left:878px;top:22px;font:400 17px/1 "Roboto",sans-serif;color:var(--ink)}

/* panel */
.panel{left:90px;top:65px;width:814px;height:891px;background:var(--panel);box-shadow:0 0 8px rgba(0,0,0,.08)}
.nav{left:113px;top:72px;width:766px;height:30px;background:var(--blue);display:flex;align-items:center;
  font:400 11px/1 "Roboto",sans-serif;color:#fff;letter-spacing:.3px}
.nav a{padding:0 12px}
.nav .home{background:var(--dark);height:30px;line-height:30px;padding:0 15px}
.nav .sep{color:#cfe8f8;padding:0 14px}

/* hero */
.hero{left:113px;top:108px;width:766px;height:305px;
  background:linear-gradient(160deg,#3b7fc8 0,#7fb7e5 35%,#c9dced 60%,#e7eef3 100%)}
.hero-title{right:141px;top:325px;text-align:right;color:#fff;text-shadow:0 1px 3px rgba(0,0,0,.5);white-space:nowrap}
.hero-title h2{font:700 23px/1 "Roboto Condensed",sans-serif;letter-spacing:.3px;margin-right:106px}
.hero-title p{font:500 15px/1 "Roboto",sans-serif;margin-top:6px}
.search{left:147px;top:144px;width:241px;height:238px;background:var(--search-bg);padding:18px 22px 0;color:#fff}
.search h3{font:500 15px/1 "Roboto",sans-serif;letter-spacing:.4px}
.search .lead{font-size:9.5px;line-height:13px;color:#5ab7f0;margin-top:6px;padding-bottom:10px;border-bottom:2px solid var(--blue)}
.search label{display:block;font-size:10px;margin:10px 0 4px 2px}
.field{height:27px;background:#fff;color:#aaa;font-size:9.5px;line-height:27px;padding-left:8px;position:relative;margin-left:2px}
.field .cal{position:absolute;right:5px;top:8px;width:10px;height:11px;border:1px solid #ccc}
.row{display:flex;gap:9px;margin-left:2px}
.select{width:91px;height:27px;background:#fff;color:#aaa;font-size:9.5px;line-height:27px;padding-left:8px;position:relative}
.select:after{content:"";position:absolute;right:6px;top:11px;border:4px solid transparent;border-top-color:#777}
.btn{width:90px;height:27px;background:var(--blue);font:500 14px/27px "Roboto",sans-serif;text-align:center}

/* section headings */
.rule{height:3px;background:var(--blue)}
.heading{font:500 14px/1 "Roboto",sans-serif;letter-spacing:.3px;color:var(--ink);white-space:nowrap}

/* featured */
.cards{left:113px;top:469px;display:flex;gap:7px}
.card{width:148px;height:181px;border:1px solid var(--line);background:#fff}
.card:first-child{box-shadow:0 2px 5px rgba(0,0,0,.25)}
.card .photo{height:113px}
.card h4{font:400 11px/1 "Roboto",sans-serif;margin:10px 0 0 7px;white-space:nowrap}
.card .price{font-size:10px;color:var(--orange);margin:6px 0 0 7px}
.card .stars{font-size:10px;color:var(--orange);letter-spacing:1px;margin:5px 0 0 7px}

/* accommodations */
.about{left:113px;top:682px;width:200px}
.about p{font:300 11.2px/18px "Roboto",sans-serif;color:var(--grey);margin-top:8px}
.tile{font-size:10px;color:var(--ink)}
.tile .photo{margin-bottom:6px}
.explore{left:687px;top:682px;width:191px}
.explore ul{list-style:none;margin-top:8px}
.explore li{font:300 11px/21px "Roboto",sans-serif;color:#666;padding-left:15px;position:relative}
.explore li:before{content:"›";position:absolute;left:0;top:-1px;color:#999;font-size:13px}
.explore li.active{color:var(--blue)}
.explore li.active:before{color:var(--blue)}

/* footer */
.foot-links{list-style:none;font:400 7.5px/17.5px "Roboto",sans-serif;color:var(--blue);text-transform:uppercase}
.foot-links li:first-child{color:var(--ink-soft)}
.foot-links.alt li:first-child{color:var(--blue)}
.ring-icon{width:18px;height:18px;border:2px solid var(--blue);border-radius:50%}
.foot-title{font:400 12px/1 "Roboto",sans-serif;color:var(--blue);letter-spacing:.2px}
.foot-text{font:400 8.5px/12.5px "Roboto",sans-serif;color:#555;width:218px}
.foot-text b{font-weight:500;color:var(--ink)}
.social{left:812px;top:976px;display:flex;gap:7px}
.social span{width:24px;height:24px;border:2px solid var(--blue);border-radius:50%}
.newsletter{left:721px;top:1015px;width:181px;height:25px;border:1px solid var(--blue);background:#fff;
  font-size:8.5px;line-height:23px;color:#888;padding-left:8px}
.newsletter i{position:absolute;right:-1px;top:-1px;width:23px;height:25px;background:var(--blue)}
.newsletter i:after{content:"";position:absolute;left:7px;top:8px;width:6px;height:6px;border:solid #fff;border-width:2px 2px 0 0;transform:rotate(45deg)}
.foot-brand{right:91px;top:1057px;text-align:right}
.foot-brand .brand-name{font-size:15px}
.foot-brand .brand-tag{font-size:5px;margin-top:2px}
.copy{right:91px;top:1088px;font-size:8.5px;color:#777}
.landscape{left:0;top:1108px;width:993px;height:78px;
  background:linear-gradient(180deg,rgba(42,155,224,0) 0,#8cc6ea 45%,#2a8bd0 100%)}
.ground{left:0;top:1183px;width:993px;height:3px;background:var(--blue)}
.base{left:0;top:1186px;width:993px;height:14px;background:var(--dark)}
</style>
</head>
<body>

<header>
  <div class="abs brand">
    <div class="brand-name">PinecrestLodgings</div>
    <div class="brand-tag">COMPARE PRICES ON ACCOMMODATIONS IN BANFF</div>
  </div>
  <div class="abs promo">Like us on Chatterly <span>for a chance to win a free 2-night stay in Banff!</span></div>
  <div class="abs round-icon promo-icon"></div>
  <div class="abs weather">Mostly Cloudy</div>
  <div class="abs weather-icon"></div>
  <div class="abs temp">0°C</div>
</header>

<main>
  <div class="abs panel"></div>

  <nav class="abs nav">
    <a class="home" href="#">HOME</a><span class="sep">/</span>
    <a href="#">BANFF HOTELS</a><span class="sep">/</span>
    <a href="#">BANFF RESORTS</a><span class="sep">/</span>
    <a href="#" style="padding:0 30px">LODGES</a><span class="sep">/</span>
    <a href="#">INNS &amp; MOTELS</a>
  </nav>

  <section>
    <div class="abs hero" role="img" aria-label="Snow-covered mountain lodge among pine trees under a bright winter sun in Banff"></div>
    <div class="abs hero-title">
      <h2>BEST SELECTION</h2>
      <p>Choose from over 47 hotels, resorts and inns in Banff</p>
    </div>
    <form class="abs search">
      <h3>SEARCH BANFF HOTELS</h3>
      <p class="lead">Enter your travel dates and find available accommodations.</p>
      <label>Check-in</label>
      <div class="field">mm/dd/yyyy<span class="cal"></span></div>
      <label style="margin-top:6px">Check-out</label>
      <div class="field">mm/dd/yyyy<span class="cal"></span></div>
      <label style="margin-top:8px">Rooms</label>
      <div class="row"><div class="select">1 Room</div><div class="btn">SEARCH</div></div>
    </form>
  </section>

  <section>
    <div class="abs rule" style="left:113px;top:429px;width:120px"></div>
    <h2 class="abs heading" style="left:113px;top:444px">FEATURED HOTELS</h2>
    <div class="abs cards">
      <article class="card"><div class="photo" role="img" aria-label="Castle-style resort lit up at night in winter" style="background:linear-gradient(180deg,#0b3f8f,#1c5fb8 60%,#2a4a6a)"></div><h4>Larchview Springs Resort</h4><div class="price">from $445 CAD</div><div class="stars">★★★★★</div></article>
      <article class="card"><div class="photo" role="img" aria-label="Indoor hot pool with stone walls" style="background:linear-gradient(180deg,#8a7a66,#b3a48e 55%,#5f6e6e)"></div><h4>Stonecleft Resort Hotel</h4><div class="price">from $445 CAD</div><div class="stars">★★★★★</div></article>
      <article class="card"><div class="photo" role="img" aria-label="Wooden mountain lodge among green trees" style="background:linear-gradient(180deg,#6f9a5c,#a06a45 55%,#4f7a3a)"></div><h4>Elkhollow Mountain Lodge</h4><div class="price">from $445 CAD</div><div class="stars">★★★★★</div></article>
      <article class="card"><div class="photo" role="img" aria-label="Hotel room with bed and fireplace" style="background:linear-gradient(180deg,#e3ddd2,#a4866c 55%,#6d3a32)"></div><h4>Corvane Royal Canadian</h4><div class="price">from $445 CAD</div><div class="stars">★★★★★</div></article>
      <article class="card"><div class="photo" role="img" aria-label="Snowy hotel buildings with mountains behind" style="background:linear-gradient(180deg,#5d9be0,#d9e4ee 40%,#9a5530 75%,#3d2a20)"></div><h4>Wren Hotel and Suites</h4><div class="price">from $445 CAD</div><div class="stars">★★★★★</div></article>
    </div>
  </section>

  <section>
    <div class="abs about">
      <div class="rule" style="width:191px"></div>
      <h2 class="heading" style="margin-top:12px">ACCOMMODATIONS IN BANFF</h2>
      <p>Banff, conveniently located in the Alberta's Rockies, is the largest city in the Banff National Park. Banff is one of the most popular tourist destinations in Canada. It is well known for its hot springs and mountainous surroundings. Tourists may enjoy a variety of activities such as hiking, biking, skiing and more.</p>
    </div>
    <a class="abs tile" href="#" style="left:336px;top:682px;width:163px"><div class="photo" role="img" aria-label="Champagne and roses on a table" style="height:98px;background:linear-gradient(160deg,#f2f2f2,#e9e2dc 55%,#c0242a)"></div>Romantic Banff getaway hotels</a>
    <a class="abs tile" href="#" style="left:336px;top:801px;width:163px"><div class="photo" role="img" aria-label="Two dogs beside luggage" style="height:98px;background:linear-gradient(180deg,#7f9aa6,#a08066 60%,#c6b7a4)"></div>Banff pet friendly hotels</a>
    <a class="abs tile" href="#" style="left:507px;top:682px;width:162px"><div class="photo" role="img" aria-label="Couple relaxing in a hot tub" style="height:217px;background:linear-gradient(180deg,#efe9e4,#d7b59b 50%,#9fd3ea 85%,#e7f4fa)"></div>Banff hotels with hot-tub</a>
    <div class="abs explore">
      <div class="rule"></div>
      <h2 class="heading" style="margin-top:13px">EXPLORE BANFF</h2>
      <ul>
        <li class="active">Things to do in Banff</li>
        <li>Banff Festivals</li>
        <li>Experience Summit Gondola</li>
        <li>Heli Sightseeing in Banff</li>
        <li>Hiking in Banff</li>
        <li>Camping &amp; Campgrounds</li>
        <li>Hotels near Upper Hot Springs</li>
        <li>Nearby Cities</li>
      </ul>
    </div>
  </section>
</main>

<footer>
  <ul class="abs foot-links" style="left:88px;top:981px">
    <li>Home</li><li>Banff Hotels</li><li>Banff Resorts</li><li>Lodges</li><li>Inns &amp; Motels</li>
  </ul>
  <ul class="abs foot-links alt" style="left:209px;top:981px;line-height:16px">
    <li>Search</li><li>Review/Cancel Reservation</li><li>Frequently Asked Questions</li><li>Privacy Policy</li><li>Terms and Conditions</li>
  </ul>
  <div class="abs ring-icon" style="left:389px;top:982px"></div>
  <h3 class="abs foot-title" style="left:417px;top:985px">HOTEL CUSTOMER SERVICE</h3>
  <p class="abs foot-text" style="left:418px;top:1002px">If you have already booked a hotel reservation and need assistance, you can contact our Customer Service at <b>877-555-0148</b>. If you call this 800 number please have your trip number, phone number and email that you entered while making your reservation available.</p>
  <div class="abs ring-icon" style="left:389px;top:1083px"></div>
  <h3 class="abs foot-title" style="left:417px;top:1086px">HOURS OF OPERATION</h3>
  <p class="abs foot-text" style="left:417px;top:1102px">24 hours a day, 7 days a week</p>

  <div class="abs" style="left:720px;top:984px;font-size:9px;color:var(--blue)">Like us on Chatterly</div>
  <div class="abs social"><span></span><span></span><span></span></div>
  <div class="abs newsletter">Newsletter signup<i></i></div>
  <div class="abs foot-brand">
    <div class="brand-name">PinecrestLodgings</div>
    <div class="brand-tag">COMPARE PRICES ON ACCOMMODATIONS IN BANFF</div>
  </div>
  <div class="abs copy">Copyright © 2016 PinecrestLodgings.net, All Rights Reserved.</div>

  <div class="abs landscape" role="img" aria-label="Silhouette of blue mountains and pine trees along the bottom edge"></div>
  <div class="abs ground"></div>
  <div class="abs base"></div>
</footer>

</body>
</html>
```